Ready to eat rice packaging design

We need packaging design for pre cooked rice of different types
1. Basmati Rice
2. Brown basmati Rice
3. Jasmine Rice
4. Lemon Rice
5. Rice Pilaf
6. Biryani Rice

Back of the package will have preparation write up and Nutrition chart.

The design should have both natural as well as modern feel to it.

Examples of packages available in market enclosed.

Target Market(s)

National Food and Grocery Stores in USA

Industry/Entity Type

Grocery Store

```html
<!DOCTYPE html>
<html lang="en">
<head>
<meta charset="utf-8">
<title>Brown Basmati Rice – Pack Front</title>
<link href="https://fonts.googleapis.com/css2?family=Fjalla+One&family=Arimo:wght@400&display=swap" rel="stylesheet">
<style>
  :root {
    --red-top: #fb4a5f;
    --red-bottom: #ae1427;
    --band-top: #8a0016;
    --band-bottom: #9a0a1d;
    --band-edge: #ff4d66;
    --dash: #ff9a3c;
    --gold-light: #ffe9a6;
    --gold-deep: #e0ad3f;
    --title: #ffffff;
    --copy: #ffffff;
    --weight-yellow: #fff36b;
  }
  html, body {
    margin: 0;
    padding: 0;
    overflow: hidden;
    background: #ffffff;
  }
  .pack {
    position: relative;
    width: 870px;
    height: 1200px;
    overflow: hidden;
  }
  .pack__art {
    position: absolute;
    inset: 0;
  }
  .title {
    position: absolute;
    left: 0;
    width: 870px;
    top: 250px;
    margin: 0;
    text-align: center;
    font-family: "Fjalla One", "Oswald", sans-serif;
    font-weight: 400;
    color: var(--title);
    line-height: 1;
    white-space: nowrap;
  }
  .title__brown {
    display: block;
    font-size: 64px;
  }
  .title__main {
    display: block;
    font-size: 104px;
    margin-top: 6px;
  }
  .copy {
    position: absolute;
    left: 252px;
    width: 366px;
    top: 548px;
    text-align: center;
    font-family: "Arimo", Arial, sans-serif;
    color: var(--copy);
  }
  .copy p {
    margin: 0;
    font-size: 24px;
    line-height: 39px;
  }
  .copy .copy__product {
    font-size: 36px;
    line-height: 48px;
  }
  .copy .copy__time {
    font-size: 39px;
    line-height: 60px;
    margin-top: 4px;
  }
  .net-weight {
    position: absolute;
    left: 0;
    width: 870px;
    top: 1092px;
    text-align: center;
    font-family: "Fjalla One", "Oswald", sans-serif;
    font-size: 38px;
    color: var(--weight-yellow);
  }
</style>
</head>
<body>
<div class="pack">
  <svg class="pack__art" width="870" height="1200" viewBox="0 0 870 1200">
    <defs>
      <linearGradient id="bg" x1="0" y1="0" x2="0" y2="1">
        <stop offset="0" stop-color="var(--red-top)"/>
        <stop offset="1" stop-color="var(--red-bottom)"/>
      </linearGradient>
      <linearGradient id="band" x1="0" y1="0" x2="0" y2="1">
        <stop offset="0" stop-color="var(--band-top)"/>
        <stop offset="1" stop-color="var(--band-bottom)"/>
      </linearGradient>
      <linearGradient id="grain" x1="0" y1="0" x2="0" y2="1">
        <stop offset="0" stop-color="var(--gold-light)"/>
        <stop offset="1" stop-color="var(--gold-deep)"/>
      </linearGradient>
    </defs>

    <rect class="bg" width="870" height="1200" fill="url(#bg)"/>

    <path class="side-arc" d="M160 90 C 60 200 60 420 200 520" fill="none" stroke="#ff6b7e" stroke-opacity="0.35" stroke-width="14"/>
    <path class="side-arc" d="M710 90 C 810 200 810 420 670 520" fill="none" stroke="#ff6b7e" stroke-opacity="0.35" stroke-width="14"/>

    <rect class="band-edge" x="225" y="0" width="30" height="1200" fill="var(--band-edge)"/>
    <rect class="band-edge" x="615" y="0" width="30" height="1200" fill="var(--band-edge)"/>
    <rect class="band" x="252" y="0" width="366" height="1200" fill="url(#band)"/>
    <line class="band-dash" x1="220" y1="0" x2="220" y2="1200" stroke="var(--dash)" stroke-width="2" stroke-dasharray="5 4"/>
    <line class="band-dash" x1="650" y1="0" x2="650" y2="1200" stroke="var(--dash)" stroke-width="2" stroke-dasharray="5 4"/>

    <rect class="stalk-art" role="img" aria-label="Golden rice stalk illustration" x="290" y="60" width="290" height="160" rx="24" fill="url(#grain)" opacity="0.85"/>
  </svg>

  <h1 class="title">
    <span class="title__brown">Brown</span>
    <span class="title__main">Basmati Rice</span>
  </h1>

  <div class="copy">
    <p>Wonderful fluffy</p>
    <p class="copy__product">Brown Basmati Rice</p>
    <p>cooked to perfection</p>
    <p>so it’s ready in</p>
    <p class="copy__time">just 90 seconds</p>
    <p>try it topped with</p>
    <p>Soy Souce and Ginger</p>
    <p>Marinated Stry-fry Beef</p>
    <p>for a super quick</p>
    <p>dinner in minutes.</p>
  </div>

  <div class="net-weight">250g</div>
</div>
</body>
</html>
```